Bedrock Yield Private Holdings Scheme

I want a professional design for a new investment program that we have designed for prospecting new prospects. We have a company logo and the content that we would like for the brochure but we would like and design structure and graphics to help compliment the content. I am attaching a rough draft of the brochure that has some

Target Market(s)

Anyone looking for hard assets, inflation hedge, cash flow investments.

```html
<!DOCTYPE html>
<html lang="en">
<head>
<meta charset="utf-8">
<title>Bedrock Yield Private Holdings Scheme – Brochure</title>
<link href="https://fonts.googleapis.com/css2?family=Montserrat:wght@700;800&family=Open+Sans:wght@400;700&display=swap" rel="stylesheet">
<style>
:root{
  --backdrop:#d7dad7;
  --paper:#ffffff;
  --green:#2f6a3c;
  --green-deep:#23502d;
  --green-pale:#e7efe8;
  --ink:#3d3d3d;
  --muted:#6b6b6b;
  --photo-gray:#9a9a9a;
  --gold:#c9a24a;
}
*{box-sizing:border-box;margin:0;padding:0}
html,body{width:914px;height:1200px;overflow:hidden}
body{background:var(--backdrop);font-family:"Open Sans",Arial,sans-serif;color:var(--ink)}
.canvas{position:relative;width:914px;height:1200px}
.spread{position:absolute;left:57px;width:800px;height:566px;display:flex;box-shadow:0 6px 18px rgba(0,0,0,.18)}
.spread--first{top:20px}
.spread--second{top:614px}
.page{position:relative;width:400px;height:566px;background:var(--paper);overflow:hidden}
.page--left{border-right:1px solid #e2e2e2}
.band{position:absolute;left:0;width:400px}
.band--top{top:0;height:22px}
.band--bottom{bottom:0;height:26px}
.page__body{position:absolute;left:30px;right:30px;top:36px;bottom:36px}
.heading{font-family:"Montserrat",Arial,sans-serif;font-weight:800;color:var(--green);line-height:1.2}
.heading--page{font-size:13px;margin-bottom:8px}
.heading--section{font-size:11.5px;margin:8px 0 3px}
.bullets{list-style:none}
.bullets li{position:relative;padding-left:10px;font-size:6.8px;line-height:1.42;margin-bottom:2px}
.bullets li::before{content:"";position:absolute;left:1px;top:3px;width:4px;height:4px;border-radius:50%;background:var(--green)}
.bullets--sub{margin-top:2px}
.bullets--sub li{padding-left:16px}
.bullets--sub li::before{left:7px;background:none;border:1px solid var(--green);width:3px;height:3px}
.bullets strong{color:#222}
.para{font-size:6.8px;line-height:1.5;margin-bottom:8px;text-align:justify}
.para--intro{font-size:6.6px;color:var(--muted);margin-bottom:10px}
.steps{display:block;margin:2px 0 4px}
.brand{position:absolute;top:30px;right:28px;display:flex;align-items:center;gap:6px;font-family:"Montserrat",Arial,sans-serif;font-weight:700;font-size:10px;color:var(--green)}
.brand__dot{width:12px;height:12px;border-radius:50%;background:var(--green)}
.photo{display:block;width:100%;border-radius:2px}
.photo--markets{height:170px;margin-bottom:12px;background:linear-gradient(135deg,#cfcfcf,#8e8e8e 60%,#bdbdbd)}
.photo--wells{height:150px;margin-bottom:6px;background:linear-gradient(180deg,#ffffff 0%,#ffffff 30%,#d9b869 70%,#a9843a 100%)}
.photo--coins{height:150px;margin:8px 0 10px;background:linear-gradient(120deg,#e8edf2,#cfd7df 50%,#d8b866 85%,#b48d3f)}
.photo--barrels{position:absolute;right:0;bottom:0;width:120px;height:74px;background:linear-gradient(160deg,#6d6d6d,#2e2e2e 60%,#8aa58a)}
.page--right .page__body--offset{top:54px}
</style>
</head>
<body>
<main class="canvas">

  <!-- Spread one -->
  <section class="spread spread--first">
    <article class="page page--left">
      <svg class="band band--top" viewBox="0 0 400 22" aria-hidden="true">
        <rect x="0" y="0" width="400" height="5" fill="var(--green)"/>
        <polygon points="0,0 60,0 48,14 0,14" fill="var(--green)"/>
      </svg>
      <div class="page__body">
        <h2 class="heading heading--page">How does the Bedrock Yield Private Holdings Scheme work?</h2>
        <svg class="steps" width="340" height="78" viewBox="0 0 340 78" aria-label="Five steps: Identify, Acquire, Manage, Reinvestment, Divestment">
          <line x1="20" y1="58" x2="320" y2="58" stroke="var(--green)" stroke-width="1"/>
          <g font-family="Montserrat, Arial, sans-serif" text-anchor="middle">
            <g transform="translate(34,0)">
              <circle cx="0" cy="24" r="19" fill="#fff" stroke="var(--green)" stroke-width="1.5"/>
              <circle cx="0" cy="24" r="15" fill="var(--green)"/>
              <polygon points="-4,42 4,42 0,50" fill="var(--green)"/>
              <circle cx="0" cy="58" r="2.5" fill="var(--green)"/>
              <text x="0" y="30" font-size="16" font-weight="700" fill="#fff">1</text>
              <text x="0" y="72" font-size="7" fill="var(--green)">Identify</text>
            </g>
            <g transform="translate(102,0)">
              <circle cx="0" cy="24" r="19" fill="#fff" stroke="var(--green)" stroke-width="1.5"/>
              <circle cx="0" cy="24" r="15" fill="var(--green)"/>
              <polygon points="-4,42 4,42 0,50" fill="var(--green)"/>
              <circle cx="0" cy="58" r="2.5" fill="var(--green)"/>
              <text x="0" y="30" font-size="16" font-weight="700" fill="#fff">2</text>
              <text x="0" y="72" font-size="7" fill="var(--green)">Acquire</text>
            </g>
            <g transform="translate(170,0)">
              <circle cx="0" cy="24" r="19" fill="#fff" stroke="var(--green)" stroke-width="1.5"/>
              <circle cx="0" cy="24" r="15" fill="var(--green)"/>
              <polygon points="-4,42 4,42 0,50" fill="var(--green)"/>
              <circle cx="0" cy="58" r="2.5" fill="var(--green)"/>
              <text x="0" y="30" font-size="16" font-weight="700" fill="#fff">3</text>
              <text x="0" y="72" font-size="7" fill="var(--green)">Manage</text>
            </g>
            <g transform="translate(238,0)">
              <circle cx="0" cy="24" r="19" fill="#fff" stroke="var(--green)" stroke-width="1.5"/>
              <circle cx="0" cy="24" r="15" fill="var(--green)"/>
              <polygon points="-4,42 4,42 0,50" fill="var(--green)"/>
              <circle cx="0" cy="58" r="2.5" fill="var(--green)"/>
              <text x="0" y="30" font-size="16" font-weight="700" fill="#fff">4</text>
              <text x="0" y="72" font-size="7" fill="var(--green)">Reinvestment</text>
            </g>
            <g transform="translate(306,0)">
              <circle cx="0" cy="24" r="19" fill="#fff" stroke="var(--green)" stroke-width="1.5"/>
              <circle cx="0" cy="24" r="15" fill="var(--green)"/>
              <polygon points="-4,42 4,42 0,50" fill="var(--green)"/>
              <circle cx="0" cy="58" r="2.5" fill="var(--green)"/>
              <text x="0" y="30" font-size="16" font-weight="700" fill="#fff">5</text>
              <text x="0" y="72" font-size="7" fill="var(--green)">Divestment</text>
            </g>
          </g>
        </svg>

        <h3 class="heading heading--section">Identify</h3>
        <ul class="bullets">
          <li>Bedrock Yield uses a proven, ongoing acquisition strategy with an expanding network to find undervalued producing oil and gas mineral interests on a weekly basis.</li>
          <li>Bedrock Yield holds these assets in its own portfolio for a short period and then transfers them to the investor's partnership or to individuals.</li>
        </ul>
        <h3 class="heading heading--section">Acquire</h3>
        <ul class="bullets">
          <li>Personal Portfolio investors acquire a diverse group of producing energy royalties with a $100,000 minimum investment.</li>
          <li>The portfolio will be adapted to the investment objectives of the investor.</li>
        </ul>
        <h3 class="heading heading--section">Manage</h3>
        <ul class="bullets">
          <li>Bedrock Yield will manage the entire acquisition process from legal documents and recording of title to notifying operators through Harlow Royalty Services, LLC, handling the taxing agencies and quarterly statements.</li>
        </ul>
        <h3 class="heading heading--section">payments.</h3>
        <ul class="bullets">
          <li>Bedrock Yield collects royalty payments and will provide monthly cash flow statements, quarterly investment statements, year end statistics and tax statements.</li>
        </ul>
        <h3 class="heading heading--section">Reinvestment</h3>
        <ul class="bullets">
          <li>Throughout the year and in alignment with the investor's objectives, Bedrock Yield will reinvest the cash flow from the initial portfolio into more royalty interests to increase the investor's asset base.</li>
          <li>At some point, at the discretion of the owner, Bedrock Yield will stop the reinvestment plan and direct all monthly payments to go straight to the owner.</li>
        </ul>
        <h3 class="heading heading--section">Divestment</h3>
        <ul class="bullets">
          <li>When the owner chooses to sell any or all of the portfolio, Bedrock Yield will assist them in the divestment by:
            <ul class="bullets bullets--sub">
              <li>Providing the necessary data and documentation</li>
              <li>Setting up the divestment for the seller with one or more outlets</li>
              <li>Managing the sale process through funding</li>
            </ul>
          </li>
        </ul>
      </div>
      <svg class="band band--bottom" viewBox="0 0 400 26" aria-hidden="true">
        <rect x="0" y="10" width="400" height="16" fill="var(--green)"/>
        <polygon points="0,0 34,0 46,26 0,26" fill="var(--green)"/>
        <polygon points="70,10 78,10 70,26 62,26" fill="#fff"/>
      </svg>
    </article>

    <article class="page page--right">
      <svg class="band band--top" viewBox="0 0 400 22" aria-hidden="true">
        <rect x="0" y="0" width="400" height="5" fill="var(--green)"/>
        <polygon points="340,0 400,0 400,14 352,14" fill="var(--green)"/>
      </svg>
      <div class="brand"><span class="brand__dot"></span>Bedrock Yield, LLC</div>
      <div class="page__body page__body--offset">
        <h2 class="heading heading--page">Bedrock Yield Private Holdings Scheme</h2>
        <p class="para para--intro">What should investors do in a volatile market? Bedrock Yield offers a way to profit from the ongoing energy transition and protect themselves from inflation with a hard asset that produces monthly cash flow.</p>
        <div class="photo photo--markets" role="img" aria-label="Black and white photo of a financial newspaper headline about where to invest money, with glasses and signposts for stocks and real estate"></div>
        <p class="para">Bedrock Yield, LLC is a successful oil and gas mineral and royalty company that has been acquiring interests in the United States for many years. Based in Texas, our team has built a proven network, rigorous due diligence and strong relationships with operators, which lets us identify and secure producing assets that deliver reliable income to our partners across changing markets and price cycles.</p>
        <p class="para">For this reason, we are now providing an exclusive opportunity for a limited number of investors to participate in the Bedrock Yield Private Holdings Scheme. This program gives investors direct ownership of a diversified group of royalty interests, professional management and the flexibility to grow, hold or sell their portfolio at any time.</p>
      </div>
      <svg class="band band--bottom" viewBox="0 0 400 26" aria-hidden="true">
        <rect x="0" y="10" width="400" height="16" fill="var(--green)"/>
        <polygon points="366,0 400,0 400,26 354,26" fill="var(--green)"/>
        <polygon points="330,10 338,10 330,26 322,26" fill="#fff"/>
      </svg>
    </article>
  </section>

  <!-- Spread two -->
  <section class="spread spread--second">
    <article class="page page--left">
      <svg class="band band--top" viewBox="0 0 400 22" aria-hidden="true">
        <rect x="0" y="0" width="400" height="5" fill="var(--green)"/>
        <polygon points="0,0 60,0 48,14 0,14" fill="var(--green)"/>
      </svg>
      <div class="page__body">
        <div class="photo photo--wells" role="img" aria-label="Illustration of oil pumpjacks standing on rising stacks of gold coins"></div>
        <h3 class="heading heading--section">What are Personal Portfolios?</h3>
        <ul class="bullets">
          <li>They are a diversified portfolio of producing oil and gas mineral royalty interests owned directly by the investor.</li>
          <li>Each portfolio is built around the investor's goals for income and growth.</li>
          <li>Investors receive a share of revenue from every well without paying drilling or operating costs.</li>
        </ul>
        <h3 class="heading heading--section">What owning a portfolio of energy royalties means for an investor?</h3>
        <ul class="bullets">
          <li>It gives the investor an <strong>investment in real assets</strong>, a proven inflation hedge.</li>
          <li>The portfolio is held in one <strong>concentrated</strong> vehicle that is easy to track.</li>
          <li>Investors gain <strong>long term monthly cash flow</strong> from producing wells.</li>
          <li>The owner has <strong>no debt, liability, or capital calls</strong>.</li>
          <li>Royalties can provide a <strong>hedge against inflation</strong>.</li>
          <li>The owner has <strong>total control</strong> over whether to hold, sell, or transfer the interests.</li>
        </ul>
        <div class="photo photo--barrels" role="img" aria-label="Photo of black oil barrels beside a stack of banknotes"></div>
      </div>
      <svg class="band band--bottom" viewBox="0 0 400 26" aria-hidden="true">
        <rect x="0" y="10" width="400" height="16" fill="var(--green)"/>
        <polygon points="0,0 34,0 46,26 0,26" fill="var(--green)"/>
        <polygon points="70,10 78,10 70,26 62,26" fill="#fff"/>
      </svg>
    </article>

    <article class="page page--right">
      <svg class="band band--top" viewBox="0 0 400 22" aria-hidden="true">
        <rect x="0" y="0" width="400" height="5" fill="var(--green)"/>
        <polygon points="340,0 400,0 400,14 352,14" fill="var(--green)"/>
      </svg>
      <div class="page__body">
        <h3 class="heading heading--section">Why Bedrock Yield, LLC?</h3>
        <ul class="bullets">
          <li>Bedrock Yield is a professional group with decades of experience evaluating, acquiring and managing mineral and royalty assets.</li>
          <li>Our process has been refined through thousands of transactions across the major producing basins in the country.</li>
        </ul>
        <div class="brand" style="position:static;justify-content:flex-end;margin-top:8px"><span class="brand__dot"></span>Bedrock Yield, LLC</div>
        <div class="photo photo--coins" role="img" aria-label="Photo of stacked gold and silver coins on a financial chart with glasses and a pen"></div>
        <h3 class="heading heading--section">Why did Bedrock Yield create the Private Holdings Scheme?</h3>
        <ul class="bullets">
          <li>Bedrock Yield's team acquires assets every month and sees how these opportunities fit the varied needs of individual investors.</li>
          <li>Many investors want the benefits of owning royalties but lack the time, data or network to build a portfolio on their own.</li>
          <li>This program gives them direct ownership with professional support at every stage of the process.</li>
          <li>Investors can choose how involved to be, from fully managed to a hands-on partnership.</li>
        </ul>
      </div>
      <svg class="band band--bottom" viewBox="0 0 400 26" aria-hidden="true">
        <rect x="0" y="10" width="400" height="16" fill="var(--green)"/>
        <polygon points="366,0 400,0 400,26 354,26" fill="var(--green)"/>
        <polygon points="330,10 338,10 330,26 322,26" fill="#fff"/>
      </svg>
    </article>
  </section>

</main>
</body>
</html>
```